Voltara Solutions Ltd - Project for new electric vehicle charging company

Please use Voltara Solutions Ltd logo & artwork instead of Brimwell.

We would like to produce a leaflet to advertise our electric vehicle charging company to build a reputation and workflow in the local area.

We would like to use the attached logo and maintain the colour palette of the of the logo to be simple, modern and effective.

I have over 15 years experience in the electrical industry and have direct access to the latest technology in electric vehicle charging.

All quotes to remain fixed costs subject to survey of the property and maintenance options can be available.

We can also offer further remedial works to any property through our sister company Brimwell Solutions Ltd.

Target Market(s)

Domestic / commercial customers

Requirements
Must have
• Voltara Solutions Ltd logo and colour palette.
Should not have
• Brimwell logo, Email or website address.

```html
<!DOCTYPE html>
<html lang="en">
<head>
<meta charset="utf-8">
<title>Voltara Solutions Ltd – EV Charging Leaflet</title>
<link rel="stylesheet" href="https://fonts.googleapis.com/css2?family=Montserrat:ital,wght@0,400;0,500;0,600;0,700;0,800;1,400;1,500;1,700;1,800&display=swap">
<style>
  :root {
    --night: #141a4a;
    --violet: #4a2a8c;
    --glow: #d23a7a;
    --teal: #27b9a8;
    --teal-dark: #17877c;
    --teal-light: #7fdccf;
    --white: #ffffff;
    --ink: #4a4f54;
    --ink-soft: #5d6368;
    --orange: #f29a12;
  }
  * { box-sizing: border-box; margin: 0; padding: 0; }
  html, body { width: 765px; height: 1200px; overflow: hidden; background: #ffffff; }
  body { font-family: "Montserrat", Arial, sans-serif; }
  .leaflet { position: relative; width: 765px; height: 1200px; overflow: hidden; background: var(--white); }
  .leaflet__art { position: absolute; inset: 0; }

  .headline {
    position: absolute; left: 42px; top: 58px;
    color: var(--white); font-weight: 800; font-style: italic;
    font-size: 46px; line-height: 1.12; letter-spacing: -0.5px;
    text-shadow: 0 2px 6px rgba(0,0,0,.35);
  }

  .plug-badge {
    position: absolute; left: 58px; top: 462px; width: 118px; height: 118px;
    border-radius: 50%; background: var(--white);
    display: flex; flex-direction: column; align-items: center; justify-content: center; gap: 6px;
  }
  .brand { display: flex; align-items: center; gap: 6px; color: var(--orange); font-weight: 700; }
  .brand__dot { width: 14px; height: 14px; border-radius: 50%; background: var(--orange); flex: none; }
  .plug-badge .brand { font-size: 17px; }
  .brand-sub { color: var(--orange); font-weight: 700; font-size: 7px; letter-spacing: 1.5px; }

  .services { position: absolute; left: 120px; top: 622px; width: 375px; list-style: none; }
  .services li { display: flex; align-items: flex-start; gap: 12px; margin-bottom: 20px; }
  .bolt { width: 26px; height: 26px; flex: none; margin-top: 2px; }
  .services__lead { color: var(--white); font-weight: 800; font-style: italic; font-size: 27px; line-height: 1.05; letter-spacing: .5px; }
  .services__item { color: var(--ink-soft); font-weight: 500; font-size: 23px; letter-spacing: .4px; white-space: nowrap; }

  .about-box {
    position: absolute; left: 515px; top: 535px; width: 215px; height: 345px;
    border: 2px solid var(--white); border-radius: 12px; padding: 14px 14px;
    color: var(--white); font-size: 14.5px; line-height: 1.5; font-weight: 500;
  }

  .footer-brand { position: absolute; left: 548px; top: 890px; display: flex; flex-direction: column; align-items: center; }
  .footer-brand .brand { font-size: 30px; }
  .footer-brand .brand-sub { font-size: 9px; margin-top: 2px; }

  .phone { position: absolute; left: 150px; top: 950px; display: flex; align-items: center; gap: 14px; }
  .icon-circle { width: 40px; height: 40px; border-radius: 50%; background: var(--ink); display: flex; align-items: center; justify-content: center; flex: none; }
  .phone__number { color: var(--ink); font-weight: 700; font-size: 40px; letter-spacing: 1px; }

  .terms {
    position: absolute; left: 60px; right: 60px; top: 1010px;
    text-align: center; color: var(--ink-soft); font-style: italic; font-size: 16.5px; line-height: 1.3;
  }

  .contacts { position: absolute; left: 58px; right: 60px; top: 1102px; display: flex; justify-content: space-between; }
  .contact { display: flex; align-items: center; gap: 12px; color: var(--ink); font-size: 17px; }
  .contact .icon-circle { width: 30px; height: 30px; background: var(--orange); }
</style>
</head>
<body>
<main class="leaflet">
  <svg class="leaflet__art" width="765" height="1200" viewBox="0 0 765 1200">
    <defs>
      <linearGradient id="photoTone" x1="0" y1="0" x2="1" y2="1">
        <stop offset="0" stop-color="#1d2a6e"/>
        <stop offset=".45" stop-color="#141a4a"/>
        <stop offset=".75" stop-color="#4a2a8c"/>
        <stop offset="1" stop-color="#2a1a5a"/>
      </linearGradient>
      <radialGradient id="photoGlow" cx=".62" cy=".35" r=".35">
        <stop offset="0" stop-color="#d23a7a" stop-opacity=".85"/>
        <stop offset="1" stop-color="#d23a7a" stop-opacity="0"/>
      </radialGradient>
      <linearGradient id="tealFade" x1="0" y1="0" x2="0" y2="1">
        <stop offset="0" stop-color="#27b9a8"/>
        <stop offset=".45" stop-color="#3cc2b2"/>
        <stop offset=".72" stop-color="#bfece5"/>
        <stop offset=".82" stop-color="#ffffff"/>
      </linearGradient>
      <radialGradient id="plugTone" cx=".5" cy=".5" r=".5">
        <stop offset="0" stop-color="#17877c" stop-opacity=".55"/>
        <stop offset="1" stop-color="#17877c" stop-opacity="0"/>
      </radialGradient>
    </defs>
    <rect width="765" height="8" fill="#0b0f30"/>
    <g role="img" aria-label="Photo of an electric car at a glowing charging station at night">
      <rect y="8" width="765" height="500" fill="url(#photoTone)"/>
      <rect y="8" width="765" height="500" fill="url(#photoGlow)"/>
    </g>
    <path d="M0,440 C180,360 330,500 500,410 C600,355 690,370 765,345 L765,360 C690,385 600,372 500,428 C330,518 180,380 0,458 Z" fill="#17877c"/>
    <path d="M0,458 C180,380 330,518 500,428 C600,372 690,385 765,360 L765,1200 L0,1200 Z" fill="url(#tealFade)"/>
    <path d="M0,458 C180,380 330,518 500,428 C600,372 690,385 765,360" fill="none" stroke="#7fdccf" stroke-width="3"/>
    <g role="img" aria-label="Illustration of a charging plug carrying the company name">
      <ellipse cx="105" cy="560" rx="105" ry="120" fill="url(#plugTone)"/>
    </g>
  </svg>

  <h1 class="headline">Over<br>15 Years<br>Experience</h1>

  <div class="plug-badge">
    <div class="brand"><span class="brand__dot"></span>Voltara</div>
    <div class="brand-sub">SOLUTIONS LTD</div>
  </div>

  <ul class="services">
    <li>
      <svg class="bolt" viewBox="0 0 28 28"><circle cx="14" cy="14" r="14" fill="#f29a12"/><path d="M16 5 L9 15 H13 L11 23 L19 12 H15 Z" fill="#fff"/></svg>
      <span class="services__lead">ELECTRIC VEHICLE<br>CHARGING...</span>
    </li>
    <li>
      <svg class="bolt" viewBox="0 0 28 28"><circle cx="14" cy="14" r="14" fill="#f29a12"/><path d="M16 5 L9 15 H13 L11 23 L19 12 H15 Z" fill="#fff"/></svg>
      <span class="services__item">DIRECT ACCESS...</span>
    </li>
    <li>
      <svg class="bolt" viewBox="0 0 28 28"><circle cx="14" cy="14" r="14" fill="#f29a12"/><path d="M16 5 L9 15 H13 L11 23 L19 12 H15 Z" fill="#fff"/></svg>
      <span class="services__item">LATEST TECHNOLOGY...</span>
    </li>
  </ul>

  <div class="about-box">
    We install home and workplace chargers with care. Every job starts with a free survey and a fixed quote. Our team handles wiring, permits and testing. Sister company Brimwell Solutions Ltd offers remedial works for any property. Ask about maintenance plans today.
  </div>

  <div class="footer-brand">
    <div class="brand"><span class="brand__dot"></span>Voltara</div>
    <div class="brand-sub">SOLUTIONS LTD</div>
  </div>

  <div class="phone">
    <span class="icon-circle">
      <svg width="22" height="22" viewBox="0 0 24 24"><path d="M6.6 10.8a15.1 15.1 0 0 0 6.6 6.6l2.2-2.2c.3-.3.7-.4 1-.2 1.1.4 2.3.6 3.6.6.6 0 1 .4 1 1V20c0 .6-.4 1-1 1A17 17 0 0 1 3 4c0-.6.4-1 1-1h3.5c.6 0 1 .4 1 1 0 1.3.2 2.5.6 3.6.1.3 0 .7-.2 1z" fill="#fff"/></svg>
    </span>
    <span class="phone__number">0123456789</span>
  </div>

  <p class="terms">All quotes to remain fixed costs subject to survey of the property and maintenance options can be available</p>

  <div class="contacts">
    <div class="contact">
      <span class="icon-circle"><svg width="16" height="16" viewBox="0 0 24 24"><rect x="2" y="5" width="20" height="14" rx="2" fill="#fff"/><path d="M3 6l9 7 9-7" fill="none" stroke="#f29a12" stroke-width="2"/></svg></span>
      <span>E mail:email address.com</span>
    </div>
    <div class="contact">
      <span class="icon-circle"><svg width="16" height="16" viewBox="0 0 24 24"><circle cx="12" cy="12" r="9" fill="none" stroke="#fff" stroke-width="2"/><path d="M3 12h18M12 3c3 3 3 15 0 18M12 3c-3 3-3 15 0 18" fill="none" stroke="#fff" stroke-width="1.6"/></svg></span>
      <span>www.your websites.com</span>
    </div>
  </div>
</main>
</body>
</html>
```